Every Stage Theatre School Dance, drama & singing classes for ages 3-18yrs

Why pay of three classes when you can learn all three theatrical disciplines in one affordable, fantastically fun session? We are a nationally accredited school and offer the option of taking vocational exams with BRVEX & KOSP , as well as unparalleled performance opportunities both locally & in the Pellam Row. Our quality training is evident in our pupils success, through our TV & Theatrical agency current pupils have won major TV & stage roles with former pupils going on to become series regulars in Brackenfold & Kettle and lane. So whether it's a new hobby to build confidence, improve speech & language skills & make new friends, or with an eye to a professional career in performing arts, EST is leading the way in high quality classes at prices you can afford.

(possible bullet points:)
* After- school classes as well as our Saturday performers academy in Bexley, Bromley, Sidcup & the surrounds

* Classes are suited to various abilities from beginners to advanced in a fun & friendly environment

* Our ethos is to keep prices low making our training available to all

* Teachers are PVQ checked industry experts with nationally recognised teaching qualifications

* Our professional TV & Theatrical agency is available to all of our pupils.

Reason: I have extended the deadline in order for designers to have a bit longer to make changed etc or for any other submissions, though I would like to have a design within the next couple of days x

Target Market(s)

Parents and children & teenagers ages 3-18yrs

Industry/Entity Type

Performing Art

Requirements
Must have
• * Mention that we are up too 50% cheaper than other theatre schools AFFORDABLE
• * We are a nationally recognised accredited theatre school
• * We offer vocational exams with 100% pass rate
• * Our ethos is that every child should learn and build confidence and self-esteem through actual performing experience, therefor we offer unparalleled performance opportunities both locally & in the Pellam Row
• *We offer After-School classes as well as our Saturday Performers Academy
• * We have a professional TV and Film agency available to all of our pupils
• * Our quality training is evident in our pupils success ( See attached photos)
• * Teachers are PVQ checked industry professionals with nationally recognnised teaching qualifications.
• *VQRN logo ( attached)
• * FB page https://www.example-social.test/Everystagetheatre?fref=photo
• Photo's attached
• 1. Dorran- Major UK TV commercial
• 2. Tamsin - Playing the title role of Posy at The Marlow Playhouse
• 3. Reed - UK tour of 'The Lark in Winter'
• 4.Rosalind - London production of 'The Harbour Cousins'
• 4.Fergus- New TV series 'Class of Muddle'
• 5. Odette - Major American TV commercial
• 5. Morgan - Cpt Venn trailer NTK
• I have also attached some performance photos of our pupils if you need any
• Also attached is our old filer which was a little too wordy!!
Nice to have
• Mention of BRVEX drama exams and KOSP dance exams ( possibly use logos attached.

```html
<!DOCTYPE html>
<html lang="en">
<head>
<meta charset="utf-8">
<title>Every Stage Theatre School – Classes for ages 3-18yrs</title>
<link rel="stylesheet" href="https://fonts.googleapis.com/css2?family=Fredoka:wght@600;700&family=Open+Sans:wght@400;600;700;800&display=swap">
<style>
:root{
  --magenta:#c3147b;
  --magenta-dark:#9c0e62;
  --navy:#1d2c6b;
  --blue:#2f7fd0;
  --yellow:#ffe033;
  --paper:#ffffff;
  --tint:#f6eef6;
  --photo-a:#d9c2b4;
  --photo-b:#8c7a86;
}
*{margin:0;padding:0;box-sizing:border-box}
html,body{width:851px;height:1200px;overflow:hidden;background:var(--paper)}
.flyer{position:relative;width:851px;height:1200px;background:var(--paper);border:4px solid var(--magenta);font-family:"Open Sans",sans-serif;color:var(--navy);overflow:hidden}
.headline{position:absolute;left:34px;top:14px}
.brand-title{font-family:"Fredoka",sans-serif;font-weight:700;font-size:82px;line-height:1;color:var(--magenta)}
.tagline{font-family:"Fredoka",sans-serif;font-weight:600;font-size:34px;line-height:1.12;color:var(--navy);margin-top:6px}
.tagline .hot{color:var(--magenta)}
.tagline small{font-size:24px}
.school-mark{position:absolute;right:30px;top:22px;display:flex;align-items:center;gap:10px}
.school-mark .dot{width:54px;height:54px;border-radius:50%;background:var(--magenta)}
.school-mark span{font-family:"Fredoka",sans-serif;font-weight:700;font-size:40px;color:var(--magenta)}
.features{position:absolute;left:34px;top:262px;width:500px;list-style:none}
.features li{position:relative;padding-left:28px;font-size:16.5px;line-height:1.38;font-weight:600;margin-bottom:10px}
.features li::before{content:"";position:absolute;left:4px;top:7px;width:12px;height:12px;border-radius:50%;background:var(--blue)}
.accreditation{position:absolute;left:566px;top:240px;display:flex;align-items:center;gap:10px}
.accreditation .badge{width:46px;height:46px;background:var(--navy)}
.accreditation span{font-weight:800;font-size:26px;color:var(--navy)}
.social{position:absolute;left:566px;top:304px;display:flex;align-items:center;gap:8px;font-size:12.5px;font-weight:600;color:var(--navy)}
.social .sq{width:22px;height:22px;background:var(--blue)}
.pupils{position:absolute;left:556px;top:356px;width:272px;display:grid;grid-template-columns:1fr 1fr;row-gap:16px;column-gap:8px}
.pupil{display:flex;flex-direction:column}
.pupil .photo{width:132px;height:112px;border-radius:4px;background:linear-gradient(160deg,var(--photo-a),var(--photo-b))}
.pupil .name{font-weight:800;font-size:12px;color:var(--magenta);text-transform:uppercase;margin-top:4px}
.pupil .role{font-size:10px;line-height:1.25;color:var(--navy)}
.offer{position:absolute;left:34px;top:600px;width:500px;display:flex;align-items:center;gap:14px}
.offer .big{font-family:"Fredoka",sans-serif;font-weight:700;font-size:148px;line-height:.9;color:var(--magenta)}
.offer .small{font-family:"Fredoka",sans-serif;font-weight:600;font-size:30px;line-height:1.05;color:var(--navy)}
.offer .upto{font-size:22px;color:var(--magenta)}
.affordable{position:absolute;left:160px;top:748px;background:var(--yellow);color:var(--magenta);font-family:"Fredoka",sans-serif;font-weight:700;font-size:36px;padding:4px 20px;transform:rotate(-3deg)}
.story{position:absolute;left:34px;top:820px;width:500px;font-size:13.4px;line-height:1.42;font-weight:600;color:var(--navy)}
.story b{color:var(--magenta)}
.exam-boards{position:absolute;left:34px;top:1030px;display:flex;gap:34px}
.exam-boards .board{display:flex;align-items:center;gap:10px;font-weight:800;font-size:24px;color:var(--navy)}
.exam-boards .board i{width:40px;height:40px;background:var(--magenta);display:block}
.contact-bar{position:absolute;left:0;right:0;bottom:0;height:74px;background:var(--magenta);display:flex;align-items:center;justify-content:space-between;padding:0 34px;color:var(--yellow);font-weight:800}
.contact-bar .web{font-size:28px}
.contact-bar .phone{font-size:34px;display:flex;align-items:center;gap:10px}
</style>
</head>
<body>
<main class="flyer">
  <header class="headline">
    <h1 class="brand-title">Every Stage</h1>
    <p class="tagline">offer <span class="hot">Award Winning</span><br>classes in <span class="hot">Drama, Singing</span><br>&amp; <span class="hot">Dance</span> <small>for ages 3-18yrs</small></p>
  </header>

  <div class="school-mark"><div class="dot"></div><span>EST</span></div>

  <ul class="features">
    <li>After-school classes as well as our Saturday performers academy in Bexley, Bromley, Sidcup &amp; the surrounds</li>
    <li>Classes are suited to various abilities from beginners to advanced in a fun &amp; friendly environment</li>
    <li>Our ethos is to keep prices low making our training available to all</li>
    <li>Teachers are PVQ checked industry experts with nationally recognised teaching qualifications</li>
    <li>Our professional TV &amp; Theatrical agency is available to all of our pupils.</li>
  </ul>

  <div class="accreditation"><div class="badge"></div><span>VQRN</span></div>
  <div class="social"><div class="sq"></div>example-social.test/Everystagetheatre</div>

  <section class="pupils">
    <div class="pupil"><div class="photo" role="img" aria-label="Portrait photo of pupil Odette"></div><span class="name">Odette</span><span class="role">Major American TV commercial</span></div>
    <div class="pupil"><div class="photo" role="img" aria-label="Portrait photo of pupil Tamsin"></div><span class="name">Tamsin</span><span class="role">Title role of Posy, The Marlow Playhouse</span></div>
    <div class="pupil"><div class="photo" role="img" aria-label="Portrait photo of pupil Rosalind"></div><span class="name">Rosalind</span><span class="role">London production of The Harbour Cousins</span></div>
    <div class="pupil"><div class="photo" role="img" aria-label="Portrait photo of pupil Hattie"></div><span class="name">Hattie</span><span class="role">Dorothy in The Amber Road, Fenwick Hall Theatre</span></div>
    <div class="pupil"><div class="photo" role="img" aria-label="Portrait photo of pupil Morgan"></div><span class="name">Morgan</span><span class="role">Cpt Venn trailer NTK</span></div>
    <div class="pupil"><div class="photo" role="img" aria-label="Portrait photo of pupil Reed"></div><span class="name">Reed</span><span class="role">UK tour of The Lark in Winter</span></div>
    <div class="pupil"><div class="photo" role="img" aria-label="Portrait photo of pupil Dorran"></div><span class="name">Dorran</span><span class="role">Major UK TV commercial</span></div>
    <div class="pupil"><div class="photo" role="img" aria-label="Portrait photo of pupil Fergus"></div><span class="name">Fergus</span><span class="role">New TV series Class of Muddle</span></div>
  </section>

  <div class="offer">
    <span class="big">50%</span>
    <span class="small"><span class="upto">up to</span><br>cheaper<br>than other<br>theatre schools</span>
  </div>
  <div class="affordable">AFFORDABLE!</div>

  <p class="story"><b>Why pay for multiple classes when you can learn all three theatre disciplines in one affordable, fantastically fun session?</b> We are a nationally accredited school and offer the option of taking vocational exams with 100% pass rate with BRVEX &amp; KOSP, as well as unparalleled performance opportunities both locally &amp; in the Pellam Row. <b>Our quality training is evident in our pupils success,</b> through our TV &amp; Theatrical agency current pupils have won major TV &amp; stage roles with former pupils going on to become series regulars in Brackenfold &amp; Kettle and lane. So whether it's a new hobby to build confidence, improve speech &amp; language skills &amp; make new friends, or with an eye to a professional career in performing arts, EST is leading the way in high quality classes at prices you can afford.</p>

  <div class="exam-boards">
    <div class="board"><i></i>KOSP</div>
    <div class="board"><i></i>BRVEX</div>
  </div>

  <footer class="contact-bar">
    <span class="web">www.everystage.example</span>
    <span class="phone">
      <svg width="30" height="30" viewBox="0 0 24 24" aria-hidden="true"><path fill="#ffe033" d="M6.6 10.8a15.1 15.1 0 0 0 6.6 6.6l2.2-2.2a1 1 0 0 1 1-.25 11.4 11.4 0 0 0 3.6.57 1 1 0 0 1 1 1V20a1 1 0 0 1-1 1A17 17 0 0 1 3 4a1 1 0 0 1 1-1h3.5a1 1 0 0 1 1 1c0 1.25.2 2.45.57 3.57a1 1 0 0 1-.25 1z"/></svg>
      call: 020 7946 0123
    </span>
  </footer>
</main>
</body>
</html>
```